URGENT website build for kids rugby company

We have created a new company that has venues all over London coaching kids age 2-7 fun rugby based activities. This is an urgent job that needs to be finished within 3 weeks.

We need a website built within the next 2-3 weeks that shows all our venues and details of each with a dedicated page that would have a location map, times or lessons, coach profiles and a "book here" button. The site must enable clients to book their "free trial" or "term membership" on the website. This will mean working with our payment company call Tallow Pay, and a CRM booking management site (to be confirmed on Monday 25th Nov). We must have the ability to create a new venue page at any time.

The front page would have a slide show of editable pictures, an intro text area under the picture frame. It would need to have a number of promo boxes on it as well.

It would have a few other pages of info such as:
A page explaining in detail our age groups of which there are 3 (red, green and blue)
how the lessons work and activity examples
terms and conditions
kit you can buy

I will give a more detailed brief on conversation with applicants for the job

It needs to be a kid AND mum friendly design. with easy and familiar usability and as uncluttered as possible. Corporate colours are red, black and white.

Industry/Entity Type

It Company

Requirements
Nice to have
• These are website designs I like and would aspire to have a similar feel to:
• http://www.brovilta-studio.com/
• http://www.quintarmolde.com/
• http://www.zelbrook.com
Should not have
• Site similar to our company include the following - but we do NOT want to look like these but the site content is relevant:
• http://www.ovenpipsters.co.uk/
• http://www.flimtoads.com/
• http://www.gramwickhoppers.com/site/

```html
<!DOCTYPE html>
<html lang="en">
<head>
<meta charset="utf-8">
<title>Scrumlings Coaching – Venue</title>
<link href="https://fonts.googleapis.com/css2?family=Open+Sans:wght@400;600;700&display=swap" rel="stylesheet">
<style>
  :root {
    --red: #c0161b;
    --red-bright: #e02026;
    --ink: #222222;
    --muted: #555555;
    --line: #e3e3e3;
    --panel: #f2f2f2;
    --footer: #3a3a3a;
    --footer-base: #2b2b2b;
    --footer-text: #bdbdbd;
    --white: #ffffff;
  }
  * { box-sizing: border-box; margin: 0; padding: 0; }
  html, body { width: 832px; height: 1200px; overflow: hidden; }
  body { font-family: "Open Sans", Arial, sans-serif; color: var(--ink); background: var(--white); position: relative; }

  .site-header { position: absolute; top: 0; left: 0; width: 832px; height: 62px; }
  .brand { position: absolute; left: 131px; top: 14px; display: flex; align-items: center; gap: 8px; }
  .brand-mark { width: 14px; height: 14px; border-radius: 50%; background: var(--red); }
  .brand-name { font-size: 16px; font-weight: 700; color: var(--red); letter-spacing: .3px; text-transform: uppercase; line-height: 1.1; width: 110px; }
  .header-contact { position: absolute; right: 127px; top: 13px; text-align: right; }
  .call { font-size: 8px; color: var(--red); }
  .social { display: flex; gap: 9px; justify-content: flex-end; margin-top: 10px; }
  .social span { width: 11px; height: 11px; border-radius: 50%; background: #333; display: block; }

  .main-nav { position: absolute; top: 62px; left: 0; width: 832px; height: 38px; border-top: 1px solid var(--line); border-bottom: 1px solid var(--line); }
  .main-nav ul { list-style: none; display: flex; position: absolute; right: 117px; top: -1px; height: 39px; }
  .main-nav li { font-size: 8.5px; text-transform: uppercase; display: flex; align-items: center; padding: 0 12px; border-left: 1px solid var(--line); color: var(--ink); }
  .main-nav li.active { background: var(--red); color: var(--white); width: 68px; justify-content: center; border-left: 0; }
  .main-nav li.about { width: 68px; justify-content: center; }
  .main-nav li.venue { width: 68px; justify-content: center; }
  .main-nav li.kit { width: 64px; justify-content: center; }
  .main-nav li.contact { width: 68px; justify-content: center; border-right: 1px solid var(--line); }

  .hero { position: absolute; top: 100px; left: 0; width: 832px; height: 258px; overflow: hidden; }
  .hero-photo { position: absolute; inset: 0; background: linear-gradient(180deg, #3f4a2e 0%, #56693a 45%, #4f7a32 70%, #3f6628 100%); }
  .hero-caption { position: absolute; left: 187px; top: 126px; width: 440px; color: var(--white); }
  .hero-caption h2 { font-size: 11.5px; font-weight: 400; line-height: 1.45; }
  .hero-caption p { font-size: 8.5px; line-height: 1.35; margin-top: 6px; }
  .hero-dots { position: absolute; left: 393px; top: 222px; display: flex; gap: 3px; }
  .hero-dots span { width: 11px; height: 11px; border-radius: 50%; background: rgba(255,255,255,.5); }
  .hero-dots span.on { background: var(--white); }
  .hero-arrow { position: absolute; top: 82px; }
  .hero-arrow.prev { left: 46px; }
  .hero-arrow.next { right: 40px; }

  .section-title { font-size: 11.5px; font-weight: 600; color: var(--red); text-transform: uppercase; padding-bottom: 4px; border-bottom: 1px solid var(--line); }
  .venue { position: absolute; left: 127px; top: 413px; width: 382px; }
  .venue .section-title { padding-left: 3px; }
  .panel { background: var(--panel); font-size: 8.5px; text-transform: uppercase; padding: 0 6px; height: 27px; display: flex; align-items: center; }
  .panel.open { color: var(--red); margin-top: 25px; }
  .map { display: block; width: 382px; height: 333px; margin-top: 9px; background: linear-gradient(160deg, #eef0e6 0%, #e3e8d6 50%, #dfe6cf 100%); }
  .panel.closed { margin-top: 7px; }
  .panel.closed + .panel.closed { margin-top: 7px; }

  .booking { position: absolute; left: 534px; top: 413px; width: 173px; }
  .booking form { padding: 10px 0 0 7px; }
  .booking label { display: block; font-size: 7.5px; color: var(--ink); margin-top: 12px; }
  .booking label:first-child { margin-top: 8px; }
  .booking .field { width: 156px; height: 25px; border: 1px solid #d6d6d6; margin-top: 8px; background: var(--white); }
  .booking .field.area { height: 98px; }
  .book-btn { display: block; margin: 11px 0 0 88px; width: 68px; height: 25px; background: var(--red-bright); color: var(--white); font-size: 8.5px; text-transform: uppercase; border: 1px solid #b51419; font-family: inherit; }

  .site-footer { position: absolute; top: 951px; left: 0; width: 832px; height: 213px; background: var(--footer); border-top: 4px solid #d8d8d8; }
  .footer-cols { position: absolute; left: 128px; top: 41px; display: flex; }
  .footer-col { width: 148px; }
  .footer-col h4 { font-size: 9px; font-weight: 400; color: var(--white); text-transform: uppercase; margin-bottom: 12px; }
  .footer-col p { font-size: 7.3px; color: var(--footer-text); line-height: 1.55; }
  .blog-date { color: var(--red-bright) !important; margin-top: 6px; }
  .contact-line { display: flex; gap: 8px; align-items: flex-start; margin-top: 14px; }
  .contact-line svg { flex: none; }
  .subscribe { display: flex; margin-top: 12px; }
  .subscribe .input { width: 93px; height: 17px; background: #2e2e2e; border: 1px solid #555; font-size: 6.5px; color: #999; padding: 4px 5px; }
  .subscribe .send { width: 42px; height: 17px; background: #262626; border: 1px solid #555; font-size: 7px; color: #aaa; text-transform: uppercase; display: flex; align-items: center; justify-content: center; margin-left: 2px; }
  .footer-base { position: absolute; top: 1164px; left: 0; width: 832px; height: 36px; background: var(--footer-base); }
  .footer-base p { position: absolute; right: 125px; top: 13px; font-size: 7.5px; color: var(--footer-text); }
</style>
</head>
<body>
  <header class="site-header">
    <div class="brand">
      <span class="brand-mark"></span>
      <span class="brand-name">Scrumlings Coaching</span>
    </div>
    <div class="header-contact">
      <p class="call">Call : +00 44 987650</p>
      <div class="social"><span></span><span></span><span></span><span></span><span></span></div>
    </div>
  </header>

  <nav class="main-nav">
    <ul>
      <li class="active">Home</li>
      <li class="about">About us</li>
      <li class="venue">Venue</li>
      <li class="kit">Rugby kit</li>
      <li class="contact">Contact us</li>
    </ul>
  </nav>

  <section class="hero">
    <div class="hero-photo" role="img" aria-label="Slideshow photo of children playing tag rugby on a grass pitch"></div>
    <svg class="hero-arrow prev" width="14" height="40" viewBox="0 0 14 40"><polyline points="12,2 2,20 12,38" fill="none" stroke="#fff" stroke-width="2"/></svg>
    <svg class="hero-arrow next" width="14" height="40" viewBox="0 0 14 40"><polyline points="2,2 12,20 2,38" fill="none" stroke="#fff" stroke-width="2"/></svg>
    <div class="hero-caption">
      <h2>Lorem ipsum dolor sit amet, consectetuer adipiscing elit, sed diam nonummy nibh euismod tincidunt ut laoreet dolore magna aliquam erat volutpat.</h2>
      <p>Ut wisi enim ad minim veniam, quis nostrud exerci tation ullamcorper suscipit lobortis nisl ut aliquip ex ea commodo consequat.</p>
    </div>
    <div class="hero-dots"><span></span><span class="on"></span><span></span></div>
  </section>

  <section class="venue">
    <h3 class="section-title">Venue</h3>
    <div class="panel open">Location map</div>
    <div class="map" role="img" aria-label="Location map of the venue area"></div>
    <div class="panel closed">Times or lessons</div>
    <div class="panel closed">Coach profile</div>
  </section>

  <aside class="booking">
    <h3 class="section-title">Book now</h3>
    <form>
      <label>Name</label><div class="field"></div>
      <label>Email</label><div class="field"></div>
      <label>Phone</label><div class="field"></div>
      <label>Comment</label><div class="field area"></div>
      <button class="book-btn" type="button">Book now</button>
    </form>
  </aside>

  <footer class="site-footer">
    <div class="footer-cols">
      <div class="footer-col">
        <h4>About us</h4>
        <p>Lorem ipsum dolor sit amet, consectetur adipisicing elit, sed do eiusmod tempor incididunt ut labore et dolore magna aliqua. Ut enim ad minim veniam, quis nostrud exercitation ullamco laboris nisi ut aliquip ex ea commodo consequat.</p>
      </div>
      <div class="footer-col">
        <h4>Latest blogs</h4>
        <p class="blog-date">24 November 2013</p>
        <p>Lorem ipsum dolor sit amet, consectetur adipisicing elit, sed do</p>
        <p class="blog-date">20 November 2013</p>
        <p>Lorem ipsum dolor sit amet, consectetur adipisicing elit, sed do</p>
      </div>
      <div class="footer-col">
        <h4>Get in touch</h4>
        <p>If you have any questions don't hesitate to contact us</p>
        <div class="contact-line">
          <svg width="8" height="11" viewBox="0 0 8 11"><path d="M4 0a4 4 0 0 0-4 4c0 3 4 7 4 7s4-4 4-7a4 4 0 0 0-4-4z" fill="#e02026"/><circle cx="4" cy="4" r="1.4" fill="#3a3a3a"/></svg>
          <p>Address: ZX4 7QL SCOTLAND. Brambleford Hall Annex R. Hallow</p>
        </div>
        <div class="contact-line">
          <svg width="9" height="9" viewBox="0 0 9 9"><path d="M1 0h2l1 2-1.2 1a5 5 0 0 0 3.2 3.2L7 5l2 1v2c0 .6-.4 1-1 1A8 8 0 0 1 0 1c0-.6.4-1 1-1z" fill="#e02026"/></svg>
          <p>Telephone: +00 44 987650321</p>
        </div>
        <div class="contact-line">
          <svg width="10" height="8" viewBox="0 0 10 8"><rect width="10" height="8" fill="#e02026"/><polyline points="0,0 5,4.5 10,0" fill="none" stroke="#3a3a3a" stroke-width="1"/></svg>
          <p>Email: info@scrumlingskids.uk</p>
        </div>
      </div>
      <div class="footer-col">
        <h4>Newsletter subscribe</h4>
        <p>Stay up to date with latest news from our company. We promise we won't spam you.</p>
        <div class="subscribe"><div class="input">Enter your email here...</div><div class="send">Send</div></div>
      </div>
    </div>
  </footer>
  <div class="footer-base"><p>copyrights 2013, All rights Reserved</p></div>
</body>
</html>
```